brisknest

i want to ues this logo and the same colors used on the business card

cleaning & service

Industry/Entity Type

Business

Contact Information for Business Card

Font styles to use
Serif
Sans Serif
Decorative
Script

Colors
add136
0692cd
000000
5c5c5c
fbfbfb

Requirements
Must have
• cleaning things

```html
<!DOCTYPE html>
<html lang="en">
<head>
<meta charset="utf-8">
<title>Brisknest — Business Card</title>
<link rel="stylesheet" href="https://fonts.googleapis.com/css2?family=Kaushan+Script&family=Quicksand:wght@500;700&display=swap">
<style>
  :root {
    --green: #add136;
    --blue: #0692cd;
    --blue-light: #13a6dc;
    --black: #000000;
    --grey: #5c5c5c;
    --paper: #fbfbfb;
    --stage: #e9ebee;
  }
  * { box-sizing: border-box; margin: 0; padding: 0; }
  html, body { width: 1200px; height: 780px; overflow: hidden; }
  body {
    background: var(--stage);
    font-family: "Quicksand", sans-serif;
    display: flex;
    align-items: center;
    justify-content: center;
    gap: 90px;
  }
  .card {
    position: relative;
    width: 340px;
    height: 580px;
    border-radius: 22px;
    overflow: hidden;
    box-shadow: 0 10px 28px rgba(0,0,0,0.18);
  }
  .card-art { position: absolute; inset: 0; width: 100%; height: 100%; }

  /* Brand lockup */
  .brand {
    position: absolute; left: 0; right: 0;
    display: flex; align-items: center; justify-content: center; gap: 10px;
  }
  .brand-dot { width: 16px; height: 16px; border-radius: 50%; background: var(--green); flex: none; }
  .brand-name {
    font-family: "Quicksand", sans-serif; font-weight: 700;
    font-size: 36px; line-height: 1; color: var(--blue); letter-spacing: 0.5px;
  }

  /* Front */
  .card--front { background: var(--paper); }
  .card--front .brand { top: 150px; }
  .holder-name {
    position: absolute; top: 318px; left: 0; right: 0; text-align: center;
    font-family: "Kaushan Script", cursive; font-size: 30px; line-height: 1.2;
    color: var(--paper);
  }
  .contact {
    position: absolute; left: 0; right: 0; text-align: center;
    color: var(--paper); font-size: 16px; font-weight: 500;
    line-height: 1.2; letter-spacing: 0.5px;
  }
  .contact-icon { display: block; margin: 0 auto 6px; width: 24px; height: 24px; }
  .contact--phone { top: 372px; }
  .contact--mail { top: 440px; }
  .contact-divider {
    position: absolute; top: 430px; left: 50px; right: 50px;
    height: 1px; background: rgba(251,251,251,0.6);
  }

  /* Back */
  .card--back {
    background: linear-gradient(160deg, var(--blue) 0%, var(--blue-light) 55%, var(--blue) 100%);
  }
  .card--back .brand { top: 196px; }
  .card--back .brand-name { color: var(--paper); font-size: 40px; }
  .back-watermark {
    position: absolute; top: 340px; left: 0; right: 0; text-align: center;
    font-weight: 700; font-size: 68px; line-height: 1; color: rgba(255,255,255,0.07);
  }
</style>
</head>
<body>

  <section class="card card--front" aria-label="Business card front">
    <svg class="card-art" viewBox="0 0 340 580" preserveAspectRatio="none" aria-hidden="true">
      <path d="M0 268 Q170 250 340 340 L340 580 L0 580 Z" fill="var(--green)"/>
      <path d="M0 282 Q170 262 340 354 L340 580 L0 580 Z" fill="var(--blue)"/>
      <path d="M70 302 Q220 290 330 352" fill="none" stroke="var(--paper)" stroke-width="2.5"/>
      <path d="M0 500 L340 522" stroke="var(--paper)" stroke-width="10"/>
      <path d="M0 506 L340 528 L340 580 L0 580 Z" fill="var(--green)"/>
    </svg>

    <div class="brand">
      <span class="brand-dot"></span>
      <span class="brand-name">brisknest</span>
    </div>

    <p class="holder-name">Dana Merrow</p>

    <div class="contact contact--phone">
      <svg class="contact-icon" viewBox="0 0 24 24" aria-hidden="true">
        <circle cx="12" cy="12" r="11" fill="none" stroke="var(--paper)" stroke-width="1.5"/>
        <path d="M8.2 6.5 L10 6.5 L11 9.2 L9.8 10.3 Q11 12.9 13.7 14.2 L14.8 13 L17.5 14 L17.5 15.8 Q17 17.5 15.2 17.5 Q7 16.5 6.5 8.8 Q6.5 6.9 8.2 6.5 Z" fill="var(--paper)"/>
      </svg>
      +1 (555) 214 3087
    </div>
    <div class="contact-divider"></div>
    <div class="contact contact--mail">
      <svg class="contact-icon" viewBox="0 0 24 24" aria-hidden="true">
        <circle cx="12" cy="12" r="11" fill="none" stroke="var(--paper)" stroke-width="1.5"/>
        <rect x="6.5" y="8" width="11" height="8" fill="var(--paper)"/>
        <path d="M6.5 8 L12 12.5 L17.5 8" fill="none" stroke="var(--blue)" stroke-width="1.2"/>
      </svg>
      hello@brisknest.com
    </div>
  </section>

  <section class="card card--back" aria-label="Business card back">
    <div class="brand">
      <span class="brand-dot"></span>
      <span class="brand-name">brisknest</span>
    </div>
    <p class="back-watermark" aria-hidden="true">brisknest</p>
    <svg class="card-art" viewBox="0 0 340 580" preserveAspectRatio="none" aria-hidden="true">
      <path d="M0 520 Q180 470 340 470 L340 580 L0 580 Z" fill="var(--green)"/>
      <path d="M0 530 Q180 484 340 482 L340 580 L0 580 Z" fill="var(--paper)"/>
      <path d="M110 520 Q230 486 330 478" fill="none" stroke="var(--blue)" stroke-width="3"/>
    </svg>
  </section>

</body>
</html>
```